BrawnCrate placard

I need a placard designed that will go in my monthly subscription boxes to describe the products inside. There must be space to write 3-5 sentences on each product.
the first area will be titled: For your flowing mane
2 for your macho glow
3 to keep you smelling macho
4 to keep you clanging and banging at the gym.
Placard will be 5inchs wide and 7inchs long

I have attached the logo and the website address must be used in the design brawncrates.com.

Target Market(s)

men between 20-50

Colors

Designer to choose colors to be used in the design.

Requirements
Must have
• My website address brawncrates.com
• 4 area to write 3-5 sentences
• 1 for your flowing mane
• 2to keep you smelling macho
• 3 to keep you clanging and banging at the gym
• 4 for your macho glow

```html
<!DOCTYPE html>
<html lang="en">
<head>
<meta charset="utf-8">
<title>BrawnCrate Placard</title>
<link rel="stylesheet" href="https://fonts.googleapis.com/css2?family=Bebas+Neue&family=Open+Sans:wght@400;600;700&display=swap">
<style>
  :root {
    --ink: #262626;
    --red: #ff3333;
    --white: #ffffff;
  }
  * { margin: 0; padding: 0; box-sizing: border-box; }
  html, body { width: 984px; height: 1200px; overflow: hidden; background: var(--ink); }
  .placard { position: relative; width: 984px; height: 1200px; background: var(--ink); overflow: hidden; font-family: "Open Sans", sans-serif; color: var(--white); }
  .header-art { position: absolute; left: 0; top: 0; width: 984px; height: 460px; }
  .brand { position: absolute; left: 162px; top: 60px; width: 200px; text-align: center; }
  .brand-dot { width: 84px; height: 84px; border-radius: 50%; background: var(--red); margin: 0 auto 12px; }
  .brand-name { font-family: "Bebas Neue", sans-serif; font-size: 44px; line-height: 1; letter-spacing: 1px; color: var(--white); }
  .product { position: absolute; width: 380px; text-align: center; }
  .product h2 { font-family: "Bebas Neue", sans-serif; font-weight: 400; font-size: 28px; line-height: 33px; letter-spacing: 0.2px; }
  .product p { font-size: 15.4px; line-height: 18.2px; margin-top: 14px; white-space: nowrap; }
  .product--mane { left: 108px; top: 486px; }
  .product--scent { left: 531px; top: 486px; }
  .product--gym { left: 102px; top: 808px; }
  .product--glow { left: 527px; top: 808px; }
  .product--gym p { margin-top: 20px; }
  .contact-bar { position: absolute; left: 0; top: 1129px; width: 984px; height: 71px; background: var(--red); display: flex; align-items: center; justify-content: center; }
  .contact-item { font-size: 20px; font-weight: 600; padding: 0 24px; line-height: 32px; }
  .contact-item + .contact-item { border-left: 2px solid var(--white); }
</style>
</head>
<body>
<div class="placard">
  <svg class="header-art" viewBox="0 0 984 460" xmlns="http://www.w3.org/2000/svg">
    <defs>
      <linearGradient id="photo-tone" x1="0" y1="0" x2="1" y2="1">
        <stop offset="0" stop-color="#1d241d"/>
        <stop offset="0.6" stop-color="#151815"/>
        <stop offset="1" stop-color="#2a2826"/>
      </linearGradient>
    </defs>
    <path role="img" aria-label="Photo of a tattooed bearded man in a black t-shirt crouching in a dark forest" fill="url(#photo-tone)"
      d="M0 0 H984 V271 C870 325 770 350 668 354 C420 356 160 250 0 87 Z"/>
    <path class="swoosh-upper" fill="var(--red)"
      d="M0 87 C160 250 420 356 668 354 C420 352 170 305 0 213 Z"/>
    <path class="swoosh-lower" fill="var(--red)"
      d="M371 353 Q682 400 984 326 V452 Q700 440 371 353 Z"/>
  </svg>

  <div class="brand">
    <div class="brand-dot"></div>
    <div class="brand-name">BrawnCrate</div>
  </div>

  <section class="product product--mane">
    <h2>For Your Flowing Mane</h2>
    <p>Lorem ipsum dolor sit amet, consectetur<br>adipiscing elit. Cras tristique volutpat eros,<br>at ultricies quam rhoncus at. Fusce laoreet<br>consectetur tellus, in hendrerit lectus. Donec<br>blandit porttitor consectetur. Donec ut<br>euismod augue, lacinia&nbsp; Lorem ipsum dolor sit<br>amet, consectetur adipiscing elit. Cras tristique<br>volutpat eros, at ultricies quam rhoncus at.<br>Fusce laoreet consectetur tellus, in hendrerit<br>lectus. Donec blandit porttitor consectetur.<br>Donec ut euismod augue, lacinia</p>
  </section>

  <section class="product product--scent">
    <h2>To Keep You Smelling Macho</h2>
    <p>Lorem ipsum dolor sit amet, consectetur<br>adipiscing elit. Cras tristique volutpat eros,<br>at ultricies quam rhoncus at. Fusce laoreet<br>consectetur tellus, in hendrerit lectus. Donec<br>blandit porttitor consectetur. Donec ut<br>euismod augue, lacinia&nbsp; Lorem ipsum dolor sit<br>amet, consectetur adipiscing elit. Cras tristique<br>volutpat eros, at ultricies quam rhoncus at.<br>Fusce laoreet consectetur tellus, in hendrerit<br>lectus. Donec blandit porttitor consectetur.<br>Donec ut euismod augue, lacinia</p>
  </section>

  <section class="product product--gym">
    <h2>To Keep You Clanging and Banging<br>at the Gym</h2>
    <p>Lorem ipsum dolor sit amet, consectetur<br>adipiscing elit. Cras tristique volutpat eros,<br>at ultricies quam rhoncus at. Fusce laoreet<br>consectetur tellus, in hendrerit lectus. Donec<br>blandit porttitor consectetur. Donec ut<br>euismod augue, lacinia&nbsp; Lorem ipsum dolor sit<br>amet, consectetur adipiscing elit. Cras tristique<br>volutpat eros, at ultricies quam rhoncus at.<br>Fusce laoreet consectetur tellus, in hendrerit<br>lectus. Donec blandit porttitor consectetur.</p>
  </section>

  <section class="product product--glow">
    <h2>For Your Macho Glow</h2>
    <p>Lorem ipsum dolor sit amet, consectetur<br>adipiscing elit. Cras tristique volutpat eros,<br>at ultricies quam rhoncus at. Fusce laoreet<br>consectetur tellus, in hendrerit lectus. Donec<br>blandit porttitor consectetur. Donec ut<br>euismod augue, lacinia&nbsp; Lorem ipsum dolor sit<br>amet, consectetur adipiscing elit. Cras tristique<br>volutpat eros, at ultricies quam rhoncus at.<br>Fusce laoreet consectetur tellus, in hendrerit<br>lectus. Donec blandit porttitor consectetur.<br>Donec ut euismod augue, lacinia<br>Donec ut euismod augue, lacinia</p>
  </section>

  <footer class="contact-bar">
    <span class="contact-item">1-800-555-0142</span>
    <span class="contact-item">info@brawncrates.com</span>
    <span class="contact-item">www.brawncrates.com</span>
  </footer>
</div>
</body>
</html>
```